Cedar Hollow responsive web design

We need a responsive, bootstrap compatible (but design only - PSD files) website design for a fly fishing shop and guide service.

Design should be very clean. Home Page design + interior page design please.

Possible Home Page Content:
Slide Show
Highlight Three Features: Guided Trips, Fly Shop, Missouri River
About

Thank you and good luck!

Shop

• This will be used on Bootstrap CMS so needs 12 column bootstrap measurements.

DESIGN ONLY NEEDED (clean PSD files), no programming required.
Need a Home Page layout and secondary page layout

Must show use of the following:
H1 - H5 font uses
link color
Dropdown for navigation bar
Button example
• No cutout images, this will be part of CMS and client needs to be able to update most content without knowing photoshop.

```html
<!DOCTYPE html>
<html lang="en">
<head>
<meta charset="utf-8">
<title>Cedar Hollow — Fly Fishing Shop</title>
<link href="https://fonts.googleapis.com/css2?family=Open+Sans:ital,wght@0,400;0,600;0,700;0,800;1,400&display=swap" rel="stylesheet">
<style>
:root{
  --ink:#333840;
  --muted:#6b7078;
  --nav:#2e3236;
  --nav-edge:#1f2225;
  --accent:#3aa3dc;
  --accent-dark:#2a86bd;
  --accent-light:#7cc8ee;
  --footer:#3a3d42;
  --footer-deep:#2c2f33;
  --footer-text:#b8bcc2;
  --btn:#4a4e54;
  --line:#e2e4e7;
  --page:#ffffff;
}
*{box-sizing:border-box;margin:0;padding:0}
html,body{width:845px;height:1200px;overflow:hidden}
body{font-family:"Open Sans",Arial,sans-serif;color:var(--ink);background:var(--page);position:relative}
a{color:inherit;text-decoration:none}

.site-header{position:absolute;left:0;top:0;width:845px;height:85px}
.brand{position:absolute;left:40px;top:12px;display:flex;align-items:center;gap:6px;font-size:15px;font-weight:800;color:var(--accent-dark)}
.brand-mark{width:14px;height:14px;background:var(--accent)}
.phone{position:absolute;left:368px;top:12px;font-size:12px;font-weight:700;display:flex;align-items:center;gap:6px}
.account-icons{position:absolute;right:50px;top:9px;display:flex;gap:5px}
.account-icons span{width:20px;height:20px;background:var(--btn);display:flex;align-items:center;justify-content:center}
.main-nav{position:absolute;left:225px;top:44px;width:575px;height:36px;background:var(--nav);border-bottom:2px solid var(--nav-edge);display:flex;align-items:stretch}
.main-nav a{color:#fff;font-size:11px;font-weight:600;padding:0 17px;display:flex;align-items:center;border-right:1px solid #43484d}
.main-nav a.active{background:var(--accent)}
.main-nav .search{margin-left:auto;border:none;padding:0 12px}

.hero{position:absolute;left:0;top:85px;width:845px;height:338px;background:linear-gradient(180deg,#b9d0dd 0%,#8eaab9 35%,#6f8f7c 55%,#8a7a58 80%,#5c5040 100%)}
.hero-caption{position:absolute;left:490px;top:88px;color:#fff}
.hero-caption h1{font-size:30px;font-weight:700;letter-spacing:-.3px;text-shadow:0 1px 3px rgba(0,0,0,.35)}
.hero-caption p{font-size:10px;font-style:italic;line-height:14px;margin-top:4px}
.hero-arrow{position:absolute;top:148px;width:26px;height:26px;border-radius:50%;background:rgba(40,44,48,.75);display:flex;align-items:center;justify-content:center}
.hero-arrow.prev{left:34px}.hero-arrow.next{right:34px}
.hero-dots{position:absolute;left:50%;bottom:12px;transform:translateX(-50%);display:flex;gap:6px}
.hero-dots span{width:8px;height:8px;border-radius:50%;background:rgba(255,255,255,.6)}
.hero-dots span.on{background:var(--accent)}

.features{position:absolute;left:79px;top:437px;width:687px;display:flex;gap:14px}
.feature{flex:1;height:141px;position:relative}
.feature-photo{position:absolute;inset:0 0 24px 0}
.feature-label{position:absolute;left:0;right:0;bottom:0;height:24px;background:var(--accent);color:#fff;font-size:10px;font-weight:700;display:flex;align-items:center;padding-left:8px}
.feature-label i{position:absolute;right:0;top:0;width:24px;height:24px;background:var(--accent-light);display:flex;align-items:center;justify-content:center}

.section-title{font-size:11px;font-weight:800;display:flex;align-items:center;gap:10px}
.section-title::after{content:"";flex:1;height:1px;background:var(--line)}
.lesson{position:absolute;left:79px;top:600px;width:687px;height:135px}
.lesson-text{position:absolute;left:0;top:0;width:455px}
.lesson-text p{font-size:8px;line-height:12px;color:var(--muted);margin-top:6px}
.read-more{position:absolute;right:0;top:110px;background:var(--btn);color:#fff;font-size:7px;padding:4px 10px}
.lesson-video{position:absolute;left:470px;top:0;width:217px;height:135px;background:linear-gradient(160deg,#c7d3db,#8c9ba6 55%,#5f6a61)}
.play{position:absolute;left:50%;top:50%;transform:translate(-50%,-50%);width:32px;height:32px;border-radius:50%;background:rgba(40,44,48,.8);display:flex;align-items:center;justify-content:center}

.products{position:absolute;left:79px;top:745px;width:687px}
.product-grid{display:flex;gap:15px;margin-top:14px}
.product{flex:1}
.product-photo{height:135px;border:1px solid var(--line);position:relative}
.product-photo .zoom{position:absolute;right:6px;top:6px}
.product h3{font-size:8px;font-weight:800;margin-top:14px}
.product p{font-size:7px;line-height:10px;color:var(--muted);margin-top:4px}
.price{font-size:11px;font-weight:700;color:var(--accent);margin-top:6px}
.product-actions{display:flex;gap:3px;margin-top:6px}
.cart-btn{background:var(--btn);color:#fff;font-size:6.5px;font-weight:700;padding:4px 6px}
.icon-btn{width:16px;background:var(--btn);display:flex;align-items:center;justify-content:center}

.site-footer{position:absolute;left:0;top:1118px;width:845px;height:82px;background:var(--footer);color:var(--footer-text);font-size:7px}
.footer-cols{position:absolute;left:79px;top:6px;width:687px;display:flex}
.footer-cols ul{list-style:none;line-height:9.5px}
.col-links{width:160px}.col-links li:first-child{color:var(--accent-light)}
.col-help{width:170px}
.col-social{width:200px}
.col-social li{display:flex;align-items:center;gap:5px;margin-bottom:3px}
.col-social li b{width:8px;height:8px;background:var(--footer-text);display:inline-block}
.newsletter{width:157px}
.newsletter h4{font-size:7px;color:#fff;font-weight:600}
.newsletter input{display:block;width:100%;height:11px;border:none;margin-top:3px;font:inherit;font-size:6px;padding-left:3px}
.send{display:inline-block;background:var(--accent);color:#fff;font-size:7px;padding:1px 6px;margin-top:3px}
.cards{display:flex;gap:3px;margin-top:4px}
.cards span{width:18px;height:10px;border-radius:2px;background:#d7dadd}
.copyright{position:absolute;left:0;bottom:0;width:845px;height:16px;background:var(--footer-deep);padding-left:79px;display:flex;align-items:center;font-size:6.5px}
</style>
</head>
<body>

<header class="site-header">
  <a class="brand" href="#"><span class="brand-mark"></span>Cedar Hollow</a>
  <div class="phone">
    <svg width="11" height="11" viewBox="0 0 24 24"><path fill="#333840" d="M6.6 10.8a15 15 0 0 0 6.6 6.6l2.2-2.2a1 1 0 0 1 1-.25 11.4 11.4 0 0 0 3.6.57 1 1 0 0 1 1 1V20a1 1 0 0 1-1 1A17 17 0 0 1 3 4a1 1 0 0 1 1-1h3.5a1 1 0 0 1 1 1c0 1.25.2 2.45.57 3.6a1 1 0 0 1-.25 1z"/></svg>
    (555) 234-5678
  </div>
  <div class="account-icons">
    <span><svg width="10" height="10" viewBox="0 0 24 24"><path fill="#fff" d="M7 18a2 2 0 1 0 0 4 2 2 0 0 0 0-4zm10 0a2 2 0 1 0 0 4 2 2 0 0 0 0-4zM2 2h3l3.6 11h9.8L21 6H7"/></svg></span>
    <span><svg width="10" height="10" viewBox="0 0 24 24"><circle cx="12" cy="8" r="4" fill="#fff"/><path fill="#fff" d="M4 21c0-4 4-6 8-6s8 2 8 6z"/></svg></span>
  </div>
  <nav class="main-nav">
    <a class="active" href="#">Home</a>
    <a href="#">About</a>
    <a href="#">Products ▾</a>
    <a href="#">Lessons &amp; Guides</a>
    <a href="#">Our Shop</a>
    <a href="#">Contact</a>
    <a class="search" href="#"><svg width="12" height="12" viewBox="0 0 24 24"><circle cx="10" cy="10" r="6" stroke="#fff" stroke-width="2.5" fill="none"/><path d="M15 15l6 6" stroke="#fff" stroke-width="2.5"/></svg></a>
  </nav>
</header>

<section class="hero" role="img" aria-label="Fishing gear, rubber boots and a fishing basket by a mountain lake">
  <div class="hero-caption">
    <h1>Fly Fishing Shop</h1>
    <p>Nullam eu eleifend tortor, id congue leo, pellentesque<br>nisl tellus, nec mattis.</p>
  </div>
  <a class="hero-arrow prev" href="#"><svg width="10" height="10" viewBox="0 0 10 10"><path d="M7 1L3 5l4 4" stroke="#fff" stroke-width="2" fill="none"/></svg></a>
  <a class="hero-arrow next" href="#"><svg width="10" height="10" viewBox="0 0 10 10"><path d="M3 1l4 4-4 4" stroke="#fff" stroke-width="2" fill="none"/></svg></a>
  <div class="hero-dots"><span class="on"></span><span></span><span></span></div>
</section>

<section class="features">
  <a class="feature" href="#">
    <div class="feature-photo" role="img" aria-label="Two anglers holding a caught fish on a river" style="background:linear-gradient(160deg,#9fb3c0,#6e8574 60%,#4f5a48)"></div>
    <div class="feature-label">GUIDED TRIPS<i><svg width="8" height="8" viewBox="0 0 10 10"><path d="M3 1l4 4-4 4" stroke="#fff" stroke-width="2" fill="none"/></svg></i></div>
  </a>
  <a class="feature" href="#">
    <div class="feature-photo" role="img" aria-label="Interior of the fly shop with rods and gear" style="background:linear-gradient(160deg,#a88a62,#7a5e3e 60%,#4d3b28)"></div>
    <div class="feature-label">FLY SHOP<i><svg width="8" height="8" viewBox="0 0 10 10"><path d="M3 1l4 4-4 4" stroke="#fff" stroke-width="2" fill="none"/></svg></i></div>
  </a>
  <a class="feature" href="#">
    <div class="feature-photo" role="img" aria-label="Missouri River valley with hills" style="background:linear-gradient(180deg,#b6cde0,#8fa6a8 45%,#7d8a5d 75%,#5a6645)"></div>
    <div class="feature-label">MISSOURI RIVER<i><svg width="8" height="8" viewBox="0 0 10 10"><path d="M3 1l4 4-4 4" stroke="#fff" stroke-width="2" fill="none"/></svg></i></div>
  </a>
</section>

<section class="lesson">
  <div class="lesson-text">
    <h2 class="section-title">LESSON AND GUIDELINE</h2>
    <p>Sed vestibulum vitae purus lacus, rutrum tincidunt. Vivamus sit amet tortor semper, vehicula turpis at, mattis est augue. Donec nec nisi dictum, in congue leo. Aliquam consectetur ligula faucibus, pellentesque ante tristique posuere, ut tellus nisl, porta sem, et dictum enim ut massa, vitae ornare dolor.</p>
    <p>Cras gravida imperdiet sapien, sit amet placerat mauris interdum id.</p>
  </div>
  <a class="read-more" href="#">Read More</a>
  <div class="lesson-video" role="img" aria-label="Video of the shop storefront under a cloudy sky">
    <span class="play"><svg width="12" height="12" viewBox="0 0 10 10"><path d="M2 1l7 4-7 4z" fill="#fff"/></svg></span>
  </div>
</section>

<section class="products">
  <h2 class="section-title">FEATURE PRODUCTS</h2>
  <div class="product-grid">
    <article class="product">
      <div class="product-photo" role="img" aria-label="Fly fishing reel" style="background:linear-gradient(#fff,#f1f2f3)">
        <svg class="zoom" width="11" height="11" viewBox="0 0 24 24"><circle cx="10" cy="10" r="6" stroke="#666" stroke-width="2.5" fill="none"/><path d="M15 15l6 6" stroke="#666" stroke-width="2.5"/></svg>
      </div>
      <h3>DOLORE IPSUM</h3>
      <p>Our company is a well known leader in fishing...</p>
      <div class="price">$349.00</div>
      <div class="product-actions"><a class="cart-btn" href="#">ADD TO CART</a><span class="icon-btn"><svg width="7" height="7" viewBox="0 0 10 10"><path d="M5 9L1 5a2 2 0 0 1 4-3 2 2 0 0 1 4 3z" fill="#fff"/></svg></span></div>
    </article>
    <article class="product">
      <div class="product-photo" role="img" aria-label="Camouflage wading boot" style="background:linear-gradient(#fff,#f1f2f3)"></div>
      <h3>DOLORE IPSUM</h3>
      <p>Our company is a well known leader in fishing...</p>
      <div class="price">$349.00</div>
      <div class="product-actions"><a class="cart-btn" href="#">ADD TO CART</a><span class="icon-btn"><svg width="7" height="7" viewBox="0 0 10 10"><path d="M5 9L1 5a2 2 0 0 1 4-3 2 2 0 0 1 4 3z" fill="#fff"/></svg></span></div>
    </article>
    <article class="product">
      <div class="product-photo" role="img" aria-label="Tackle box with colorful lures" style="background:linear-gradient(#fff,#f1f2f3)"></div>
      <h3>DOLORE IPSUM</h3>
      <p>Our company is a well known leader in fishing...</p>
      <div class="price">$349.00</div>
      <div class="product-actions"><a class="cart-btn" href="#">ADD TO CART</a><span class="icon-btn"><svg width="7" height="7" viewBox="0 0 10 10"><path d="M5 9L1 5a2 2 0 0 1 4-3 2 2 0 0 1 4 3z" fill="#fff"/></svg></span></div>
    </article>
    <article class="product">
      <div class="product-photo" role="img" aria-label="Canvas fishing bag" style="background:linear-gradient(#fff,#f1f2f3)"></div>
      <h3>DOLORE IPSUM</h3>
      <p>Our company is a well known leader in fishing...</p>
      <div class="price">$349.00</div>
      <div class="product-actions"><a class="cart-btn" href="#">ADD TO CART</a><span class="icon-btn"><svg width="7" height="7" viewBox="0 0 10 10"><path d="M5 9L1 5a2 2 0 0 1 4-3 2 2 0 0 1 4 3z" fill="#fff"/></svg></span></div>
    </article>
  </div>
</section>

<footer class="site-footer">
  <div class="footer-cols">
    <ul class="col-links"><li>Home</li><li>About Us</li><li>Products</li><li>Lessons and Guides</li><li>Our Shop</li><li>Contact</li></ul>
    <ul class="col-help"><li>Register now</li><li>Delivery</li><li>Order history</li><li>Terms &amp; conditions</li><li>Security &amp; privacy</li></ul>
    <ul class="col-social"><li><b></b>Friendwall</li><li><b></b>Chirper</li><li><b></b>Circleup</li><li><b></b>Feed</li></ul>
    <div class="newsletter">
      <h4>Newsletter Subscription</h4>
      <input type="text" placeholder="Name">
      <input type="text" placeholder="Email">
      <span class="send">Send</span>
      <div class="cards"><span></span><span></span><span></span><span></span></div>
    </div>
  </div>
  <div class="copyright">Copyright © 2014 Cedar Hollow. All Rights Reserved.</div>
</footer>

</body>
</html>
```